Cake Bakery needs Large New Vibrant Window Decals

Our cake bakery is moving to a new location. We want to place window decals (vinyl) on 7 separate windows that are all the same size. (Image is attached for your reference. The windows are the ones within the red outline.)

The windows are approximately 76 inches tall and 98 inches wide. We have uploaded an image of the storefront to show you the 7 windows that need be to covered.

There are also 2 side by side doors that need a decals too. We have uploaded a logo we are using. You are allowed to change the logo color to better coordinate with a design you can create.

We want the colors to be bright and cheerful. You can see our current bakery website at brindlewoodsweets.example. ( I included the sign above our bakery if that helps you.)

Do not use any images of cakes or other bakery products in your design.

The graphics can be simple and clean or can be vivid and loud. We will consider all concepts.

You can create one design to be duplicated for each window or create a design that would flow across all the windows in a landscape effect.

Target Market(s)

People who purchase cakes for any occasion.

Industry/Entity Type

Bakery

Requirements
Must have
• Must have the logo on each window
Nice to have
• Open to any concepts
Should not have
• No images of cakes or other bakery products. The graphics must stand the test of time for the next 10 years.

```html
<!DOCTYPE html>
<html lang="en">
<head>
<meta charset="utf-8">
<title>Brindlewood Sweets — Window Decal Layout</title>
<link rel="stylesheet" href="https://fonts.googleapis.com/css2?family=Fredoka:wght@500;600;700&display=swap">
<style>
  :root{
    --backdrop:#c8c8c8;
    --frame:#ffffff;
    --glass:#484544;
    --coral:#ef8078;
    --coral-soft:#f39b8c;
    --blush:#f7c6bb;
    --cream:#ffffff;
    --plum:#542d78;
  }
  *{box-sizing:border-box;margin:0;padding:0}
  html,body{width:1200px;height:1117px;overflow:hidden}
  body{background:var(--backdrop);position:relative;font-family:"Fredoka",sans-serif}

  .pane{position:absolute;background:var(--frame);border-radius:6px;padding:8px;
        box-shadow:0 4px 6px rgba(0,0,0,.22)}
  .pane--slim{padding:7px}
  .glass{position:relative;width:100%;height:100%;background:var(--glass);overflow:hidden}

  .band{position:absolute;left:0;right:0;top:70px;height:148px;
        background:linear-gradient(90deg,var(--blush) 0%,var(--cream) 18%,var(--blush) 34%,var(--cream) 50%,var(--blush) 66%,var(--cream) 82%,var(--blush) 100%)}
  .band--door{top:35px}
  .band--door-low{top:39px}
  .band--plain{background:var(--blush)}
  .band--fade-right{background:linear-gradient(90deg,var(--blush) 0%,var(--cream) 60%,var(--cream) 100%)}
  .band--fade-left{background:linear-gradient(90deg,var(--cream) 0%,var(--cream) 40%,var(--blush) 100%)}
  .band--door-card{background:linear-gradient(90deg,var(--blush),#fbe0d9 50%,var(--blush))}

  .trim{position:absolute;left:0;right:0;height:17px;background:var(--coral)}
  .trim--top{top:0;border-bottom:3px solid var(--plum);height:21px}
  .trim--bottom{bottom:0;border-top:3px solid var(--plum);height:21px}

  .ribbon{position:absolute;left:0;right:0;top:62px;height:23px;background:var(--plum);
          box-shadow:0 -4px 0 var(--coral-soft),0 4px 0 var(--coral-soft)}
  .ribbon__text{position:absolute;top:50%;transform:translate(-50%,-50%);white-space:nowrap;
                color:#fff;font-weight:600;font-size:7px;letter-spacing:.1px}
  .ribbon__text--left{left:16%}
  .ribbon__text--right{left:84%}

  .nameplate{position:absolute;top:26px;left:50%;transform:translateX(-50%);width:137px;height:97px;
             background:#fff;border:3px solid var(--plum);border-radius:20px;
             box-shadow:inset 0 0 0 3px var(--coral-soft);
             display:flex;align-items:center;justify-content:center;text-align:center}
  .brand-name{color:var(--coral);font-weight:600;font-size:16px;line-height:1.05}

  .callout{position:absolute;left:0;right:0;top:26px;text-align:center;color:var(--plum);font-weight:700}
  .callout__pre{font-size:10px;letter-spacing:1px}
  .callout__word{display:block;color:var(--coral);font-size:34px;line-height:.95}
  .callout__post{font-size:11px}
  .callout__phone{margin-top:10px;font-size:9px;display:flex;justify-content:center;align-items:center;gap:2px}

  .door-brand{position:absolute;left:598px;top:884px;transform:translateX(-50%);
              color:var(--coral);font-weight:600;font-size:25px;line-height:1.05;text-align:center;white-space:nowrap}
</style>
</head>
<body>

<!-- Row 1 windows -->
<div class="pane" style="left:24px;top:31px;width:385px;height:305px"><div class="glass">
  <div class="band"><div class="trim trim--top"></div><div class="ribbon"><span class="ribbon__text ribbon__text--left">CAKES AND SMILES</span><span class="ribbon__text ribbon__text--right">CAKES AND SMILES</span></div>
  <div class="nameplate"><span class="brand-name">Brindlewood<br>Sweets</span></div><div class="trim trim--bottom"></div></div>
</div></div>
<div class="pane" style="left:409px;top:31px;width:385px;height:305px"><div class="glass">
  <div class="band"><div class="trim trim--top"></div><div class="ribbon"><span class="ribbon__text ribbon__text--left">CAKES AND SMILES</span><span class="ribbon__text ribbon__text--right">CAKES AND SMILES</span></div>
  <div class="nameplate"><span class="brand-name">Brindlewood<br>Sweets</span></div><div class="trim trim--bottom"></div></div>
</div></div>
<div class="pane" style="left:792px;top:31px;width:385px;height:305px"><div class="glass">
  <div class="band"><div class="trim trim--top"></div><div class="ribbon"><span class="ribbon__text ribbon__text--left">CAKES AND SMILES</span><span class="ribbon__text ribbon__text--right">CAKES AND SMILES</span></div>
  <div class="nameplate"><span class="brand-name">Brindlewood<br>Sweets</span></div><div class="trim trim--bottom"></div></div>
</div></div>

<!-- Row 2 windows -->
<div class="pane" style="left:120px;top:383px;width:386px;height:304px"><div class="glass">
  <div class="band"><div class="trim trim--top"></div><div class="ribbon"><span class="ribbon__text ribbon__text--left">CAKES AND SMILES</span><span class="ribbon__text ribbon__text--right">CAKES AND SMILES</span></div>
  <div class="nameplate"><span class="brand-name">Brindlewood<br>Sweets</span></div><div class="trim trim--bottom"></div></div>
</div></div>
<div class="pane" style="left:504px;top:383px;width:386px;height:304px"><div class="glass">
  <div class="band"><div class="trim trim--top"></div><div class="ribbon"><span class="ribbon__text ribbon__text--left">CAKES AND SMILES</span><span class="ribbon__text ribbon__text--right">CAKES AND SMILES</span></div>
  <div class="nameplate"><span class="brand-name">Brindlewood<br>Sweets</span></div><div class="trim trim--bottom"></div></div>
</div></div>

<!-- Side door with call-out -->
<div class="pane pane--slim" style="left:890px;top:383px;width:190px;height:44px"><div class="glass"></div></div>
<div class="pane" style="left:907px;top:428px;width:153px;height:286px"><div class="glass">
  <div class="band band--door band--door-card"><div class="trim trim--top"></div>
    <div class="callout">
      <span class="callout__pre">NEED A</span>
      <span class="callout__word">Cake</span>
      <span class="callout__post">RIGHT NOW?</span>
      <div class="callout__phone">
        <svg width="9" height="9" viewBox="0 0 24 24" aria-hidden="true"><path fill="#ef8078" d="M6.6 10.8a15 15 0 0 0 6.6 6.6l2.2-2.2c.3-.3.7-.4 1-.2 1.1.4 2.3.6 3.6.6.6 0 1 .4 1 1V20c0 .6-.4 1-1 1A17 17 0 0 1 3 4c0-.6.4-1 1-1h3.5c.6 0 1 .4 1 1 0 1.3.2 2.5.6 3.6.1.3 0 .7-.2 1z"/></svg>
        <span>555.014.CAKE (0199)</span>
      </div>
    </div>
  <div class="trim trim--bottom"></div></div>
</div></div>

<!-- Row 3 windows -->
<div class="pane" style="left:48px;top:754px;width:385px;height:305px"><div class="glass">
  <div class="band"><div class="trim trim--top"></div><div class="ribbon"><span class="ribbon__text ribbon__text--left">CAKES AND SMILES</span><span class="ribbon__text ribbon__text--right">CAKES AND SMILES</span></div>
  <div class="nameplate"><span class="brand-name">Brindlewood<br>Sweets</span></div><div class="trim trim--bottom"></div></div>
</div></div>
<div class="pane" style="left:765px;top:754px;width:387px;height:305px"><div class="glass">
  <div class="band"><div class="trim trim--top"></div><div class="ribbon"><span class="ribbon__text ribbon__text--left">CAKES AND SMILES</span><span class="ribbon__text ribbon__text--right">CAKES AND SMILES</span></div>
  <div class="nameplate"><span class="brand-name">Brindlewood<br>Sweets</span></div><div class="trim trim--bottom"></div></div>
</div></div>

<!-- Main double doors: transoms -->
<div class="pane pane--slim" style="left:432px;top:754px;width:57px;height:37px"><div class="glass"></div></div>
<div class="pane pane--slim" style="left:489px;top:754px;width:218px;height:37px"><div class="glass"></div></div>
<div class="pane pane--slim" style="left:707px;top:754px;width:60px;height:37px"><div class="glass"></div></div>

<!-- Main double doors: leaves -->
<div class="pane pane--slim" style="left:432px;top:794px;width:57px;height:292px"><div class="glass">
  <div class="band band--door-low band--fade-right"><div class="trim trim--top"></div><div class="trim trim--bottom"></div></div>
</div></div>
<div class="pane pane--slim" style="left:487px;top:794px;width:112px;height:292px"><div class="glass">
  <div class="band band--door-low band--fade-right"><div class="trim trim--top"></div><div class="trim trim--bottom"></div></div>
</div></div>
<div class="pane pane--slim" style="left:598px;top:794px;width:112px;height:292px"><div class="glass">
  <div class="band band--door-low band--fade-left"><div class="trim trim--top"></div><div class="trim trim--bottom"></div></div>
</div></div>
<div class="pane pane--slim" style="left:707px;top:794px;width:60px;height:292px"><div class="glass">
  <div class="band band--door-low band--plain"><div class="trim trim--top"></div><div class="trim trim--bottom"></div></div>
</div></div>
<div class="door-brand">Brindlewood<br>Sweets</div>

</body>
</html>
```